A suite of 3-4 brand templates.

I would like various brand templates using my brand colours(see my logo) that I can add information to, so I can create different help guides/ infographics on various health and well being topics (anxiety, breathing techniques, pain relief, self hypnosis etc) that I can put on my website:-
www.brightlanewellness.com

I want to ability to add both text guides and other guides to be more visual.

Target Market(s)

Health and wellbeing clients (particularly people looking for hypnosis, pain reprocessing therapy, and health coaching.

Industry/Entity Type

Health and Psychology

Font styles to use
Sans Serif

Colors
0054AA
0677BA
7BADD7
CADEEF
E8F1F8
0094D4
00A9DD
6FCCEA
C7EBF8
E9F6FB
F0912C
F2A743
F7CA91
FBE8D2
FDF5EE

Requirements
Must have
• Brand colours, website and Logo
Nice to have
• To look visually appealing and professional.

```html
<!DOCTYPE html>
<html lang="en">
<head>
<meta charset="utf-8">
<title>Intrusive Thoughts – Brightlane Wellness</title>
<link href="https://fonts.googleapis.com/css2?family=Poppins:wght@400;600;700&display=swap" rel="stylesheet">
<style>
  :root{
    --navy:#1f4e8c;
    --brand-blue:#0054AA;
    --cyan:#00A9DD;
    --sky:#0094D4;
    --orange:#F0912C;
    --amber:#F2A743;
    --ink:#1b1b1b;
    --white:#ffffff;
  }
  *{margin:0;padding:0;box-sizing:border-box}
  html,body{width:1200px;height:917px;overflow:hidden;background:var(--white)}
  body{font-family:'Poppins',sans-serif;color:var(--ink)}
  .sheet{position:relative;width:1200px;height:917px;overflow:hidden;background:var(--white)}
  .backdrop{position:absolute;inset:0}
  .brand{position:absolute;left:40px;top:60px;width:270px;text-align:center}
  .brand-mark{width:110px;height:110px;border-radius:50%;background:var(--brand-blue);margin:0 auto 18px}
  .brand-name{font-weight:600;font-size:26px;line-height:1.1;color:var(--brand-blue);letter-spacing:.5px}
  .hero-illustration{position:absolute;left:856px;top:52px;width:62px;height:62px;border-radius:50%;background:var(--orange)}
  .title{position:absolute;left:588px;width:600px;top:128px;text-align:center;color:var(--white);font-weight:700;font-size:54px;line-height:1.2}
  .subtitle{position:absolute;left:588px;width:600px;top:218px;text-align:center;color:var(--white);font-size:15px}
  .point{position:absolute;width:340px;font-size:11px;line-height:17px}
  .point h3{font-size:12.5px;font-weight:700;margin-bottom:3px}
  .point.left{text-align:right}
  .point.c-cyan h3{color:var(--sky)}
  .point.c-navy h3{color:var(--navy)}
  .point.c-orange h3{color:var(--orange)}
  .cycle{position:absolute;left:0;top:0}
  .cycle-label{position:absolute;left:554px;top:472px;width:100px;text-align:center;font-weight:700;font-size:15px;line-height:21px;color:var(--navy)}
  .tips{position:absolute;left:40px;top:708px;width:1140px;display:grid;grid-template-columns:repeat(4,1fr);row-gap:16px;column-gap:0}
  .tip{display:flex;gap:14px;align-items:flex-start;font-size:12.5px;line-height:16px}
  .tip-dot{flex:none;width:26px;height:26px;border-radius:50%;background:var(--cyan);margin-top:2px}
  .footer{position:absolute;left:0;top:852px;width:1200px;height:43px;background:var(--navy);color:var(--white);display:flex;align-items:center;justify-content:center;font-weight:600;font-size:15px;letter-spacing:5px}
</style>
</head>
<body>
<main class="sheet">
  <svg class="backdrop" width="1200" height="917" viewBox="0 0 1200 917" aria-hidden="true">
    <path d="M388 0H1200V330C1100 300 950 255 800 268C650 280 500 320 385 335C470 230 470 70 388 0Z" fill="var(--navy)"/>
    <path d="M372 0C450 70 462 230 384 338C520 322 700 284 800 272C950 258 1100 300 1200 336V344C1100 312 950 278 800 288C650 300 450 348 300 356C180 360 80 320 0 262V254C90 312 190 342 290 336C420 322 486 210 440 90C424 50 400 20 372 0Z" fill="var(--orange)"/>
    <path d="M362 0C420 50 440 150 420 210" fill="none" stroke="var(--cyan)" stroke-width="4"/>
    <path d="M250 360C450 354 650 304 800 294C950 284 1100 318 1200 348" fill="none" stroke="var(--cyan)" stroke-width="3"/>
  </svg>

  <div class="brand">
    <div class="brand-mark"></div>
    <p class="brand-name">BRIGHTLANE<br>WELLNESS</p>
  </div>

  <div class="hero-illustration" role="img" aria-label="Illustration of a head with a thought bubble"></div>
  <h1 class="title">Intrusive Thoughts</h1>
  <p class="subtitle">Lorem Ipsum is simply dummy text.</p>

  <section class="point left c-cyan" style="left:108px;top:394px">
    <h3>Lorem Ipsum</h3>
    <p>Lorem Ipsum is simply dummy text of the printing and<br>typesetting industry. Lorem Ipsum has been the industry's</p>
  </section>
  <section class="point left c-navy" style="left:57px;top:484px">
    <h3>Lorem Ipsum</h3>
    <p>Lorem Ipsum is simply dummy text of the printing and<br>typesetting industry. Lorem Ipsum has been the industry's</p>
  </section>
  <section class="point left c-orange" style="left:108px;top:585px">
    <h3>Lorem Ipsum</h3>
    <p>Lorem Ipsum is simply dummy text of the printing and<br>typesetting industry. Lorem Ipsum has been the industry's</p>
  </section>
  <section class="point c-orange" style="left:760px;top:394px">
    <h3>Lorem Ipsum</h3>
    <p>Lorem Ipsum is simply dummy text of the printing and<br>typesetting industry. Lorem Ipsum has been the industry's</p>
  </section>
  <section class="point c-navy" style="left:810px;top:484px">
    <h3>Lorem Ipsum</h3>
    <p>Lorem Ipsum is simply dummy text of the printing and<br>typesetting industry. Lorem Ipsum has been the industry's</p>
  </section>
  <section class="point c-cyan" style="left:760px;top:585px">
    <h3>Lorem Ipsum</h3>
    <p>Lorem Ipsum is simply dummy text of the printing and<br>typesetting industry. Lorem Ipsum has been the industry's</p>
  </section>

  <svg class="cycle" width="1200" height="917" viewBox="0 0 1200 917" aria-hidden="true">
    <g fill="none" stroke-width="5" stroke-linecap="round">
      <circle cx="553" cy="422" r="44" pathLength="360" stroke-dasharray="280 80" transform="rotate(-258 553 422)" stroke="var(--cyan)"/>
      <circle cx="654" cy="422" r="44" pathLength="360" stroke-dasharray="280 80" transform="rotate(-202 654 422)" stroke="var(--amber)"/>
      <circle cx="505" cy="517" r="44" pathLength="360" stroke-dasharray="280 80" transform="rotate(40 505 517)" stroke="var(--navy)"/>
      <circle cx="700" cy="517" r="44" pathLength="360" stroke-dasharray="280 80" transform="rotate(-140 700 517)" stroke="var(--navy)"/>
      <circle cx="553" cy="608" r="44" pathLength="360" stroke-dasharray="280 80" transform="rotate(-21 553 608)" stroke="var(--amber)"/>
      <circle cx="654" cy="608" r="44" pathLength="360" stroke-dasharray="280 80" transform="rotate(-79 654 608)" stroke="var(--cyan)"/>
    </g>
    <g>
      <circle cx="553" cy="419" r="7" fill="var(--cyan)"/>
      <rect x="549" y="427" width="8" height="6" rx="1" fill="var(--cyan)"/>
      <circle cx="654" cy="422" r="12" fill="var(--orange)"/>
      <circle cx="505" cy="517" r="11" fill="none" stroke="var(--navy)" stroke-width="3"/>
      <path d="M505 511V517L509 520" fill="none" stroke="var(--navy)" stroke-width="2.5" stroke-linecap="round"/>
      <rect x="689" y="510" width="22" height="16" rx="2" fill="var(--navy)"/>
      <rect x="696" y="506" width="8" height="5" rx="1" fill="none" stroke="var(--navy)" stroke-width="2"/>
      <path d="M545 608L551 614L562 601" fill="none" stroke="var(--orange)" stroke-width="3.5" stroke-linecap="round" stroke-linejoin="round"/>
      <circle cx="654" cy="608" r="12" fill="var(--sky)"/>
    </g>
  </svg>
  <p class="cycle-label">HEADING<br>GOES<br>HERE</p>

  <section class="tips">
    <div class="tip"><span class="tip-dot"></span><p>Lorem Ipsum is simply<br>dummy text of the printing<br>and typesetting industry.</p></div>
    <div class="tip"><span class="tip-dot"></span><p>Lorem Ipsum is simply<br>dummy text of the printing<br>and typesetting industry.</p></div>
    <div class="tip"><span class="tip-dot"></span><p>Lorem Ipsum is simply<br>dummy text of the printing<br>and typesetting industry.</p></div>
    <div class="tip"><span class="tip-dot"></span><p>Lorem Ipsum is simply<br>dummy text of the printing<br>and typesetting industry.</p></div>
    <div class="tip"><span class="tip-dot"></span><p>Lorem Ipsum is simply<br>dummy text of the printing<br>and typesetting industry.</p></div>
    <div class="tip"><span class="tip-dot"></span><p>Lorem Ipsum is simply<br>dummy text of the printing<br>and typesetting industry.</p></div>
    <div class="tip"><span class="tip-dot"></span><p>Lorem Ipsum is simply<br>dummy text of the printing<br>and typesetting industry.</p></div>
    <div class="tip"><span class="tip-dot"></span><p>Lorem Ipsum is simply<br>dummy text of the printing<br>and typesetting industry.</p></div>
  </section>

  <footer class="footer">www.brightlanewellness.com</footer>
</main>
</body>
</html>
```